Business Card Design for an Investment Company

We need a business card design for our private investment company, called Ashbourne Partners. Ashbourne Partners is an investments partnership that aims to acquire shares in listed companies with a view to influencing those companies through active dialogue in order to improve their value. We need designs that use the logo colors (blue, grey, white), we need both English and Arabic on the business cards (can be on one side or 2 sides). The final logo should communicate professionalism, conservatism (nothing too fancy or too cheesy), that we are smart, conservative and old school.

Target Market(s)

Investment companies

Industry/Entity Type

Investment

Contact Information for Business Card

Khalid Yousef Rumaithi
Senior Executive Officer

Palm Terrace 07, Level 3, Office 215/12
HLMZ

+9714987650
krumaithi@ashbournepartners.com
www.ashbournepartners.com

Requirements
Must have
• Logo to be placed on the left hand side of the business card
• for the Arabic, we only need to have the name and title so it can be accomodated on one side so we can have the other side with full color and logo. The arabic that needs to be used is the below:
• خالد يوسف الرميثي
• المدير التنفيدي

```html
<!DOCTYPE html>
<html lang="en">
<head>
<meta charset="utf-8">
<title>Ashbourne Partners – Business Cards</title>
<link rel="stylesheet" href="https://fonts.googleapis.com/css2?family=Open+Sans:wght@400;600;700&family=Noto+Kufi+Arabic:wght@400;700&display=swap">
<style>
  :root {
    --backdrop: #d9dadc;
    --card-grey: #5a5a5c;
    --brand-blue: #0a6fa6;
    --ink-grey: #4d4d4f;
    --paper: #ffffff;
  }
  * { margin: 0; padding: 0; box-sizing: border-box; }
  html, body {
    width: 1200px; height: 900px; overflow: hidden;
    background: var(--backdrop);
    font-family: "Open Sans", Arial, sans-serif;
  }
  .canvas { position: relative; width: 1200px; height: 900px; }

  .card {
    position: absolute;
    width: 630px; height: 360px;
    box-shadow: 0 10px 28px rgba(0,0,0,0.22);
    overflow: hidden;
  }

  /* Back side */
  .card-back {
    left: 70px; top: 60px;
    background: var(--card-grey);
    color: var(--paper);
  }
  .card-back .wordmark {
    position: absolute; left: 0; right: 0; top: 128px;
    text-align: center;
    font-size: 46px; font-weight: 700; letter-spacing: -0.5px;
  }
  .card-back .web {
    position: absolute; left: 0; right: 0; top: 268px;
    text-align: center;
    font-size: 19px; letter-spacing: 1.5px;
  }

  /* Front side */
  .card-front {
    left: 500px; top: 480px;
    background: var(--paper);
  }
  .card-front .blue-field { position: absolute; inset: 0; }
  .card-front .wordmark {
    position: absolute; left: 36px; top: 104px;
    font-size: 27px; font-weight: 700; letter-spacing: -0.3px;
    color: var(--brand-blue);
    white-space: nowrap;
  }
  .arabic-block {
    position: absolute; right: 24px; top: 16px;
    direction: rtl; text-align: right;
    color: var(--paper);
    font-family: "Noto Kufi Arabic", "Open Sans", sans-serif;
  }
  .arabic-block .ar-name { font-size: 15px; font-weight: 700; line-height: 26px; }
  .arabic-block .ar-title { font-size: 11px; line-height: 20px; }
  .name-band {
    position: absolute; left: 350px; top: 112px;
    background: var(--brand-blue);
    color: var(--paper);
    font-size: 16px; font-weight: 700;
    padding: 6px 18px 6px 22px;
    white-space: nowrap;
    clip-path: polygon(5% 0, 100% 0, 100% 100%, 0 100%);
  }
  .title-band {
    position: absolute; left: 440px; top: 148px;
    background: var(--brand-blue);
    color: var(--paper);
    font-size: 12px;
    padding: 5px 16px 5px 18px;
    white-space: nowrap;
    clip-path: polygon(6% 0, 100% 0, 100% 100%, 0 100%);
  }
  .contact {
    position: absolute; left: 42px; top: 210px;
    color: var(--ink-grey);
    font-size: 14px; line-height: 20px;
  }
  .contact .company { color: var(--brand-blue); }
  .contact .address { padding-left: 16px; }
  .contact-list { list-style: none; margin-top: 6px; padding-left: 42px; }
  .contact-list li { display: flex; align-items: center; gap: 10px; height: 24px; }
  .contact-list .icon {
    width: 20px; height: 20px;
    background: var(--brand-blue);
    display: flex; align-items: center; justify-content: center;
  }
</style>
</head>
<body>
<main class="canvas">

  <section class="card card-back" aria-label="Business card, back">
    <div class="wordmark">Ashbourne Partners</div>
    <div class="web">www.ashbournepartners.com</div>
  </section>

  <section class="card card-front" aria-label="Business card, front">
    <svg class="blue-field" width="630" height="360" viewBox="0 0 630 360" aria-hidden="true">
      <polygon points="300,0 630,0 630,250" fill="var(--brand-blue)"/>
    </svg>

    <div class="wordmark">Ashbourne Partners</div>

    <div class="arabic-block" lang="ar">
      <div class="ar-name">خالد يوسف الرميثي</div>
      <div class="ar-title">المدير التنفيدي</div>
    </div>

    <div class="name-band">Khalid Yousef Rumaithi</div>
    <div class="title-band">Senior Executive Officer</div>

    <div class="contact">
      <div class="company">Ashbourne Partners</div>
      <div class="address">Palm Terrace 07, Level 3,<br>Office 215/12 HLMZ</div>
      <ul class="contact-list">
        <li>
          <span class="icon">
            <svg width="12" height="12" viewBox="0 0 24 24" aria-hidden="true"><path fill="#fff" d="M6.6 10.8a15.1 15.1 0 0 0 6.6 6.6l2.2-2.2a1 1 0 0 1 1-.25 11.4 11.4 0 0 0 3.6.57 1 1 0 0 1 1 1V20a1 1 0 0 1-1 1A17 17 0 0 1 3 4a1 1 0 0 1 1-1h3.5a1 1 0 0 1 1 1c0 1.25.2 2.45.57 3.6a1 1 0 0 1-.25 1z"/></svg>
          </span>+9714987650
        </li>
        <li>
          <span class="icon">
            <svg width="12" height="12" viewBox="0 0 24 24" aria-hidden="true"><rect x="2" y="5" width="20" height="14" fill="none" stroke="#fff" stroke-width="2"/><path d="M2 5l10 8 10-8" fill="none" stroke="#fff" stroke-width="2"/></svg>
          </span>krumaithi@ashbournepartners.com
        </li>
        <li>
          <span class="icon">
            <svg width="12" height="12" viewBox="0 0 24 24" aria-hidden="true"><g fill="none" stroke="#fff" stroke-width="2"><circle cx="12" cy="12" r="9"/><ellipse cx="12" cy="12" rx="4" ry="9"/><path d="M3 12h18"/></g></svg>
          </span>www.ashbournepartners.com
        </li>
      </ul>
    </div>
  </section>

</main>
</body>
</html>
```